Wordpress Design for my Consulting Company

We want a WordPress site created for our new business. We have created a mock-up of the content we want on the site at https://marcusdellow.example-sites.com/website-5

We are not attached to any of the pictures and just put stock stuff from wix's editor, which we don't have rights to use outside of wix.

We are NOT looking to just port this site to WordPress, we are looking for some creative ways to display the content in a more professional artistic sense.

I have included several logo files and a text file with the colors and Fonts used in the logo. We are not looking to change the logo or the colors used in the logo.

The Schedule appointment links to a page that embeds a bookingnest.example.com calendar. https://bookingnest.example.com/marcus-dellow/brightvale

The final website domain will be enterprisebrightvale.example

Enterprise brightvale is a consulting company that works directly with the business owners and leaders of small businesses between 50-200 employees. We help companies make sure they have the right technology to meet their strategic goals. We are the anti-"Computer Guy" and we focus on business outcomes NOT cool technology gadgets.

The final design should communicate business growth and success.

Target Market(s)

Business Owners of companies with 50-200 employees

Coding

Coded - Design and coding required

Number of Pages Required

1 page

Font styles to use
Serif
Other font styles liked:
• Trajan Pro Bold, Open Sans

Requirements
Must have
• Should focus on consulting rather than technology.
• Should show the customer as the hero and we are just their guide.
• Must use the logo provided and the colors and fonts in the text file provided. Any other colors and fonts must be complementary.
• The design should scale for all devices computer, iPad, or phone
Should not have
• Should not focus on technology, we are the anti-"Computer Guy" and we focus on business outcomes NOT cool technology gadgets.

```html
<!DOCTYPE html>
<html lang="en">
<head>
<meta charset="utf-8">
<title>Brightvale – Technology Advisors</title>
<link href="https://fonts.googleapis.com/css2?family=Cinzel:wght@400;700&family=Open+Sans:wght@400;600;700&display=swap" rel="stylesheet">
<style>
:root{
  --orange:#c97a4c;
  --orange-soft:#e9a57a;
  --slate:#2f4550;
  --slate-mid:#566d78;
  --grey-bg:#f3f3f3;
  --text:#3a3a3a;
  --white:#ffffff;
}
*{box-sizing:border-box;margin:0;padding:0}
html,body{width:1200px;height:1200px;overflow:hidden;background:var(--white)}
body{font-family:"Open Sans",Arial,sans-serif;color:var(--text);position:relative}
.page{position:absolute;left:321px;top:0;width:698px;height:1500px;transform:scale(.8);transform-origin:0 0;background:var(--white);overflow:hidden;box-shadow:0 0 0 1px #eee}
.abs{position:absolute}
.serif{font-family:"Cinzel",Georgia,serif}

/* header */
.topline{left:0;top:2px;width:100%;height:2px;background:var(--orange)}
.brand{left:94px;top:10px;display:flex;align-items:center;gap:6px}
.brand-dot{width:18px;height:18px;border-radius:50%;background:var(--slate)}
.brand-name{font-family:"Cinzel",serif;font-weight:700;font-size:11px;color:var(--slate);line-height:1}
.nav{right:95px;top:16px;display:flex;gap:24px;font-size:9px;color:#555}
.nav .active{color:var(--orange);text-decoration:underline}

/* hero */
.hero{left:0;top:37px;width:100%;height:209px;background:linear-gradient(160deg,#5d84ad 0%,#a9c3dc 45%,#e8eef4 70%,#7f9fc2 100%)}
.hero-photo{left:0;top:0;width:100%;height:100%}
.hero-copy{left:262px;top:63px;width:358px;text-align:center;color:var(--slate)}
.hero-copy h1{font-family:"Cinzel",serif;font-weight:700;font-size:21px;line-height:19px}
.hero-copy p{font-family:"Cinzel",serif;font-weight:700;font-size:10px;line-height:11px;margin-top:7px}
.btn{display:inline-block;background:var(--orange);color:var(--white);font-weight:700;font-size:9px;border-radius:12px;padding:5px 9px;border:2px solid #f0c4a6}
.hero-copy .btn{margin-top:12px}
.hero-arrow{top:72px;width:14px;height:50px}

/* value circles */
.val{top:262px;width:124px;height:167px}
.val-ring{left:0;top:0;width:124px;height:124px;border-radius:50%;background:var(--slate);padding:7px}
.val-fill{width:110px;height:110px;border-radius:50%;background:var(--orange);border:2px solid #e8b08c;display:flex;flex-direction:column;align-items:center;justify-content:center;color:var(--white);text-align:center}
.val-fill svg{margin-bottom:4px}
.val-fill span{font-family:"Cinzel",serif;font-weight:700;font-size:11px;line-height:13px}
.val-stem{left:60px;top:122px;width:4px;height:44px;background:var(--slate)}
.val-base{left:45px;top:163px;width:34px;height:3px;background:var(--slate)}
.rule{left:0;top:427px;width:100%;height:1px;background:#e9c3ab}
.pager{top:438px;width:16px;height:12px;border-radius:6px}

/* tired section */
.tired{left:0;top:459px;width:100%;height:226px;background:var(--grey-bg)}
.tired-kicker{left:0;top:28px;width:100%;text-align:center;font-family:"Cinzel",serif;font-weight:700;font-size:10px;color:var(--slate)}
.tired-title{left:0;top:37px;width:100%;text-align:center;font-family:"Cinzel",serif;font-weight:700;font-size:22px;color:var(--slate)}
.tired-line{left:264px;top:67px;width:160px;height:1px;background:#999}
.tired-accent{left:339px;top:67px;width:20px;height:2px;background:var(--orange)}
.card{width:168px;height:43px}
.card-box{left:16px;top:0;width:152px;height:43px;background:var(--orange);border:1px solid #b66a3e;color:var(--white);font-size:8px;line-height:9px;padding:9px 6px 0 28px}
.card-icon{left:0;top:3px;width:37px;height:37px;border-radius:50%;background:var(--slate);border:3px solid #e0e0e0;display:flex;align-items:center;justify-content:center}

/* steps */
.steps-left{left:0;top:685px;width:466px;height:304px;background:linear-gradient(100deg,#6f8794,#566d78 60%,#44606c)}
.steps-right{left:466px;top:685px;width:232px;height:304px;background:var(--orange)}
.steps-copy{left:95px;top:786px;color:var(--white)}
.steps-copy .k{font-family:"Cinzel",serif;font-weight:700;font-size:12px}
.steps-copy h2{font-family:"Cinzel",serif;font-weight:700;font-size:21px;line-height:22px;margin-top:2px}
.steps-copy .s{font-family:"Cinzel",serif;font-size:8px;letter-spacing:3px;margin-top:6px}
.step{left:428px;width:260px;height:80px}
.step-circle{left:0;top:0;width:80px;height:80px;border-radius:50%;background:#e9e9e9;border:4px solid #c9c9c9;display:flex;flex-direction:column;align-items:center;justify-content:center;color:var(--slate);font-family:"Cinzel",serif;font-weight:700;font-size:9.5px}
.step-circle svg{margin-bottom:2px}
.step-text{left:92px;top:31px;width:150px;color:var(--white);font-size:7.5px;line-height:9.5px}
.step-text b{font-weight:600;font-size:8.5px}
.step-rule{left:92px;top:-16px;width:140px;height:1px;background:#d68c60}

/* leaders */
.leaders{left:92px;top:1038px;width:290px;text-align:center;color:var(--slate)}
.leaders .k{font-family:"Cinzel",serif;font-weight:700;font-size:11px}
.leaders h2{font-family:"Cinzel",serif;font-weight:700;font-size:21px;line-height:22px}
.leaders p{font-size:8.5px;line-height:13px;color:#555;margin-top:6px}
.leaders .btn{margin-top:13px}
.photo{width:76px;height:96px;background:#fff;border:1px solid #ddd;padding:6px;box-shadow:0 1px 3px rgba(0,0,0,.15)}
.photo div{width:100%;height:100%}

/* contact */
.map{left:0;top:1233px;width:100%;height:247px;background:linear-gradient(135deg,#d9d9d9,#ececec 50%,#dcdcdc);border-top:2px solid var(--orange)}
.contact{left:93px;top:1247px;width:510px;height:220px;background:rgba(233,140,90,.92);border:1px solid var(--orange)}
.contact h2{position:absolute;left:19px;top:37px;font-family:"Cinzel",serif;font-weight:700;font-size:25px;color:var(--white)}
.info{position:absolute;left:19px;color:var(--white);font-size:9.5px;line-height:13px;display:flex;gap:12px}
.info svg{flex:none;margin-top:1px}
.field{position:absolute;height:15px;border:1px solid #f7c9ad;color:var(--white);font-size:7px;padding:2px 4px}
.submit{position:absolute;left:337px;top:174px;width:68px;height:22px;border-radius:11px;background:var(--slate);color:var(--white);font-weight:700;font-size:10px;text-align:center;line-height:22px}
.footer{left:0;top:1480px;width:100%;height:20px;background:var(--slate);color:#ddd;font-size:6px;text-align:center;line-height:20px}
</style>
</head>
<body>
<div class="page">

  <div class="abs topline"></div>
  <div class="abs brand"><div class="brand-dot"></div><div class="brand-name">Brightvale</div></div>
  <nav class="abs nav"><span class="active">Home</span><span>Schedule</span><span>Appointment</span></nav>

  <section class="abs hero">
    <div class="abs hero-photo" role="img" aria-label="Businessman seen from behind looking up at a bright cloudy sky" style="background:linear-gradient(90deg,rgba(47,69,80,.35) 0%,rgba(255,255,255,0) 40%)"></div>
    <svg class="abs hero-arrow" style="left:12px" viewBox="0 0 14 50"><path d="M13 1 L1 25 L13 49" fill="none" stroke="#fff" stroke-width="1"/></svg>
    <svg class="abs hero-arrow" style="left:672px" viewBox="0 0 14 50"><path d="M1 1 L13 25 L1 49" fill="none" stroke="#fff" stroke-width="1"/></svg>
    <div class="abs hero-copy">
      <h1>Technology Advisors That<br>"Get" Business.</h1>
      <p>We help you leverage technology to create<br>a competitive advantage.</p>
      <span class="btn">Schedule Appointment</span>
    </div>
  </section>

  <div class="abs val" style="left:94px">
    <div class="abs val-ring"><div class="val-fill">
      <svg width="24" height="22" viewBox="0 0 24 22"><rect x="2" y="14" width="4" height="7" fill="#fff"/><rect x="9" y="10" width="4" height="11" fill="#fff"/><rect x="16" y="6" width="4" height="15" fill="#fff"/><path d="M2 10 L10 4 L14 7 L21 1" stroke="#fff" stroke-width="1.6" fill="none"/></svg>
      <span>We Get…<br>Scaling Up</span></div></div>
    <div class="abs val-stem"></div><div class="abs val-base"></div>
  </div>
  <div class="abs val" style="left:287px">
    <div class="abs val-ring"><div class="val-fill">
      <svg width="22" height="24" viewBox="0 0 22 24"><rect x="2" y="3" width="18" height="2" fill="#fff"/><rect x="8" y="0" width="6" height="3" fill="none" stroke="#fff"/><rect x="4" y="6" width="14" height="17" fill="none" stroke="#fff" stroke-width="1.6"/><path d="M8 9v11M11 9v11M14 9v11" stroke="#fff"/></svg>
      <span>We Get…<br>Eliminating<br>Bottlenecks</span></div></div>
    <div class="abs val-stem"></div><div class="abs val-base"></div>
  </div>
  <div class="abs val" style="left:480px">
    <div class="abs val-ring"><div class="val-fill">
      <svg width="28" height="28" viewBox="0 0 28 28" fill="none" stroke="#fff"><circle cx="14" cy="14" r="3"/><circle cx="14" cy="3" r="2"/><circle cx="14" cy="25" r="2"/><circle cx="3" cy="8" r="2"/><circle cx="25" cy="8" r="2"/><circle cx="3" cy="20" r="2"/><circle cx="25" cy="20" r="2"/><path d="M14 5v6M14 17v6M5 9l6 4M23 9l-6 4M5 19l6-4M23 19l-6-4"/></svg>
      <span>We Get…<br>Preparing for<br>Disruption</span></div></div>
    <div class="abs val-stem"></div><div class="abs val-base"></div>
  </div>
  <div class="abs rule"></div>
  <div class="abs pager" style="left:331px;background:var(--orange)"></div>
  <div class="abs pager" style="left:351px;background:var(--slate)"></div>

  <section class="abs tired">
    <div class="abs tired-kicker">Are you tired of</div>
    <div class="abs tired-title">"Computer Guys" that…</div>
    <div class="abs tired-line"></div><div class="abs tired-accent"></div>

    <div class="abs card" style="left:95px;top:92px"><div class="abs card-box">Don't want to be involved in business strategy.</div><div class="abs card-icon"><svg width="16" height="14"><circle cx="4" cy="4" r="2.5" fill="none" stroke="#fff"/><rect x="8" y="6" width="2" height="6" fill="#fff"/><rect x="12" y="3" width="2" height="9" fill="#fff"/></svg></div></div>
    <div class="abs card" style="left:265px;top:92px"><div class="abs card-box">Give you the excuse,<br>"You never asked."</div><div class="abs card-icon"><svg width="16" height="16"><circle cx="8" cy="5" r="4" fill="#fff"/><path d="M2 16 Q8 7 14 16Z" fill="#fff"/></svg></div></div>
    <div class="abs card" style="left:435px;top:92px"><div class="abs card-box" style="padding-top:8px">Say "No!" but do not give options on how to achieve your business outcome.</div><div class="abs card-icon"><svg width="16" height="14"><rect x="1" y="9" width="2" height="4" fill="#fff"/><rect x="5" y="7" width="2" height="6" fill="#fff"/><rect x="9" y="5" width="2" height="8" fill="#fff"/><path d="M1 6 L8 2 L15 1" stroke="#fff" fill="none"/></svg></div></div>

    <div class="abs card" style="left:95px;top:147px"><div class="abs card-box" style="padding-top:4px;line-height:8.5px">Recommend technology when a simple process or policy change would have the same effect.</div><div class="abs card-icon"><svg width="16" height="14" fill="none" stroke="#fff"><rect x="1" y="1" width="5" height="4"/><rect x="10" y="9" width="5" height="4"/><path d="M6 3h5v6"/></svg></div></div>
    <div class="abs card" style="left:265px;top:147px"><div class="abs card-box" style="padding-top:4px;line-height:8.5px">Can't explain how a technology will create business value, but insist it is necessary.</div><div class="abs card-icon"><svg width="16" height="16" fill="none" stroke="#fff"><circle cx="9" cy="5" r="4"/><path d="M1 13 Q6 9 10 12 L15 10"/></svg></div></div>
    <div class="abs card" style="left:435px;top:147px"><div class="abs card-box" style="padding-top:6px">Suggest expensive solutions that are just thrown away soon after they are deployed.</div><div class="abs card-icon"><svg width="16" height="16"><circle cx="6" cy="5" r="3.5" fill="#fff"/><path d="M1 15 Q6 8 11 15Z" fill="#fff"/><circle cx="13" cy="6" r="2" fill="none" stroke="#fff"/></svg></div></div>
  </section>

  <div class="abs steps-left" role="img" aria-label="Hand touching a screen of hand-drawn business strategy sketches"></div>
  <div class="abs steps-right"></div>
  <div class="abs steps-copy">
    <div class="k">The Four Steps to Aligning</div>
    <h2>Technology to Your<br>Business Strategy!</h2>
    <div class="s">DISCOVER YOUR BUSINESS PATH</div>
  </div>
  <div class="abs step" style="top:701px">
    <div class="abs step-circle"><svg width="18" height="18" fill="none" stroke="#c97a4c" stroke-width="2.4"><circle cx="7" cy="7" r="5"/><path d="M11 11l6 6"/></svg>Discover</div>
    <div class="abs step-text"><b>Identify what is going on behind</b><br>the scenes, and create a snapshot of the current infrastructure.</div>
  </div>
  <div class="abs step" style="top:801px">
    <div class="abs step-circle"><svg width="18" height="22" fill="none" stroke="#c97a4c" stroke-width="1.4"><rect x="2" y="3" width="14" height="18"/><rect x="6" y="1" width="6" height="3"/><path d="M5 9h8M5 13h8M5 17h8"/></svg>Prioritize</div>
    <div class="abs step-rule"></div>
    <div class="abs step-text"><b>Meet to decide which solutions</b><br>and policies will have the greatest impact on reaching the companies goals.</div>
  </div>
  <div class="abs step" style="top:901px">
    <div class="abs step-circle"><svg width="36" height="20" fill="none" stroke="#c97a4c" stroke-width="1.6"><circle cx="7" cy="8" r="5"/><path d="M5 14h4v4H5z"/><circle cx="20" cy="10" r="3"/><circle cx="30" cy="8" r="3"/><path d="M20 4v2M20 14v2M14 10h2M24 10h2M30 2v2M30 12v2M24 8h2M34 8h2"/></svg>Implement</div>
    <div class="abs step-rule"></div>
    <div class="abs step-text"><b>Implement those things that</b><br>will give the greatest return on investment.</div>
  </div>

  <div class="abs leaders">
    <div class="k">Computer Guys Frustrate</div>
    <h2>Business Leaders</h2>
    <p>Computer guys frustrate business leaders because they don't have a business mindset. Brightvale advises on strategy that helps companies apply technology to gain a competitive advantage.</p>
    <span class="btn">Schedule Appointment</span>
  </div>
  <div class="abs photo" style="left:447px;top:1009px"><div role="img" aria-label="Businesswoman at a meeting" style="background:linear-gradient(160deg,#b07c5a,#4a4a5a)"></div></div>
  <div class="abs photo" style="left:527px;top:1021px"><div role="img" aria-label="Business leader in an office" style="background:linear-gradient(160deg,#e8eef3,#6f8aa6)"></div></div>
  <div class="abs photo" style="left:447px;top:1109px"><div role="img" aria-label="Team hands joined together" style="background:linear-gradient(180deg,#9fb2c4,#324a63)"></div></div>
  <div class="abs photo" style="left:527px;top:1121px"><div role="img" aria-label="Business handshake" style="background:linear-gradient(160deg,#f4f6fa,#8f9fba)"></div></div>

  <div class="abs map" role="img" aria-label="Road map of the United States"></div>
  <section class="abs contact">
    <h2>Contact Us</h2>
    <div class="info" style="top:78px"><svg width="16" height="16" fill="none" stroke="#fff"><path d="M8 15 C3 9 3 7 3 6 a5 5 0 0 1 10 0 c0 1 0 3-5 9z"/><circle cx="8" cy="6" r="2"/></svg><div>1418 Larkspur Parkway South,<br>Suite 200 Millbrook, TX<br>77990</div></div>
    <div class="info" style="top:126px;font-weight:700;font-size:11.5px"><svg width="16" height="16" fill="none" stroke="#fff" stroke-width="1.5"><path d="M3 2 l3 0 l1 4 l-2 1 q2 4 5 5 l1-2 l4 1 l0 3 q-9 1-12-12z"/></svg><div>(555) 014-0580</div></div>
    <div class="info" style="top:152px;font-size:9px"><svg width="16" height="12" fill="none" stroke="#fff"><rect x="1" y="1" width="14" height="10"/><path d="M1 1 L8 7 L15 1"/></svg><div>mdellow@enterprisebrightvale.example</div></div>
    <div class="field" style="left:241px;top:48px;width:128px">First Name</div>
    <div class="field" style="left:373px;top:48px;width:128px">Last Name</div>
    <div class="field" style="left:241px;top:71px;width:260px">Phone Number</div>
    <div class="field" style="left:241px;top:93px;width:260px">Email</div>
    <div class="field" style="left:241px;top:115px;width:260px;height:50px;padding-top:5px">Subject</div>
    <div class="submit">Submit</div>
  </section>
  <footer class="abs footer">©2018 by Enterprise brightvale</footer>
</div>
</body>
</html>
```